Bref créative
Velmoran Group
Business Cards and Letterhead
Professional
Peter L. Dunmore
Founder
2700 Fenwick Lane
Suite 500
Massapequa Park, NY 11594
TBD
pete@velmoran-example.com
www.velmoran-example.com
We need to incorporate a tagline under the logo stating," Real Estate Development and Diversified Investments".
Here is where I would like to see some creativity! This is a growing, dynamic new company, so, bring your ideas.
Please try some designs with this alternate logo with black background.

```html
<!DOCTYPE html>
<html lang="en">
<head>
<meta charset="utf-8">
<title>Velmoran Group – Stationery Options</title>
<link href="https://fonts.googleapis.com/css2?family=Open+Sans:wght@400;600;700&family=Arimo:wght@700&display=swap" rel="stylesheet">
<style>
  :root{
    --bg:#ece9e4;
    --paper:#ffffff;
    --navy:#0d2a5c;
    --blue:#1d5fae;
    --sky:#6fa6dd;
    --ink:#2b3440;
    --muted:#8a93a0;
    --label:#7a5a3c;
    --dark:#0a1630;
    --rule:#b7bec8;
  }
  *{box-sizing:border-box;margin:0;padding:0}
  html,body{width:1200px;height:452px;overflow:hidden;background:var(--bg);font-family:"Open Sans",Arial,sans-serif;color:var(--ink)}
  .canvas{position:relative;width:1200px;height:452px}
  .option-label{position:absolute;top:36px;font-family:"Arimo",Arial,sans-serif;font-weight:700;font-size:27px;color:var(--label)}
  .sheet{position:absolute;top:92px;width:226px;height:336px;background:var(--paper);box-shadow:0 2px 6px rgba(0,0,0,.25)}
  .brand{display:flex;flex-direction:column;align-items:center;gap:3px}
  .brand-dot{width:18px;height:18px;border-radius:50%;background:radial-gradient(circle at 35% 35%,var(--sky),var(--navy))}
  .brand-name{font-weight:700;font-size:7px;letter-spacing:.6px;color:var(--navy);text-transform:uppercase;white-space:nowrap}
  .sheet .brand{position:absolute;top:10px;left:0;right:0}
  .decor{position:absolute;left:22px;top:96px;width:150px;height:150px;border-radius:50%;background:radial-gradient(circle at 45% 40%,#ffffff 0%,#eef1f5 55%,#dde3ea 100%)}
  .sheet-footer{position:absolute;left:0;right:0;bottom:14px}
  .sheet-footer p{font-size:4.5px;color:var(--muted);padding:0 14px 3px;white-space:nowrap}
  .band{height:8px;background:linear-gradient(90deg,var(--navy),var(--blue) 45%,var(--sky) 70%,#e8eef6)}
  .band-dot{position:absolute;left:50%;top:9px;width:12px;height:12px;margin-left:-6px;border-radius:50%;background:radial-gradient(circle at 35% 35%,var(--sky),var(--navy))}
  .fax-title{position:absolute;left:14px;top:58px;font-weight:700;font-size:13px;color:var(--ink)}
  .fax-fields{position:absolute;left:14px;right:14px;top:78px;display:grid;grid-template-columns:1fr 1fr;column-gap:12px;row-gap:6px}
  .fax-fields span{font-size:5px;border-bottom:.5px solid var(--rule);padding-bottom:2px}
  .fax-checks{position:absolute;left:14px;right:10px;top:136px;display:flex;gap:6px}
  .fax-checks span{font-size:4.5px;display:flex;align-items:center;gap:2px;white-space:nowrap}
  .fax-checks i{display:inline-block;width:4px;height:4px;border:.5px solid var(--ink)}
  .fax-rule{position:absolute;left:14px;right:14px;top:148px;border-top:.5px solid var(--rule)}
  .envelope{position:absolute;background:var(--paper);box-shadow:0 2px 6px rgba(0,0,0,.25);overflow:hidden}
  .envelope-back{left:842px;top:22px;width:346px;height:140px}
  .envelope-back .flap{position:absolute;left:0;top:0;width:100%;height:78px}
  .envelope-front{left:872px;top:136px;width:316px;height:92px}
  .envelope-front .brand{position:absolute;left:14px;top:10px;align-items:flex-start}
  .envelope-front .band{position:absolute;left:0;right:0;bottom:0}
  .envelope-front .decor{left:auto;right:26px;top:8px;width:76px;height:76px}
  .cards{position:absolute;left:828px;top:282px;display:grid;grid-template-columns:repeat(3,116px);grid-auto-rows:70px;gap:10px 8px}
  .card{position:relative;border-radius:2px;box-shadow:0 1px 4px rgba(0,0,0,.3);overflow:hidden}
  .card-light{background:var(--paper)}
  .card-dark{background:radial-gradient(circle at 30% 40%,#1d3d78,var(--dark) 70%)}
  .card .brand{position:absolute;left:8px;top:8px;flex-direction:row;gap:4px}
  .card .brand-dot{width:12px;height:12px}
  .card .brand-name{font-size:5px}
  .card-dark .brand-name{color:#ffffff}
  .card-contact{position:absolute;left:8px;bottom:12px;font-size:4px;line-height:1.35;color:var(--ink);white-space:nowrap}
  .card-contact strong{font-size:5px;color:var(--navy)}
  .card .band{position:absolute;left:0;right:0;bottom:0;height:6px}
  .card-dark .card-contact{color:#cfd8e6}
  .card-dark .card-contact strong{color:#ffffff}
</style>
</head>
<body>
<div class="canvas">

  <span class="option-label" style="left:98px">Option_1</span>
  <span class="option-label" style="left:356px">Option_2</span>
  <span class="option-label" style="left:615px">Option_3</span>

  <section class="sheet letterhead" style="left:43px">
    <div class="brand"><span class="brand-dot"></span><span class="brand-name">Velmoran Group</span></div>
    <div class="decor" role="img" aria-label="Soft white emblem shape as watermark"></div>
    <div class="sheet-footer">
      <p>2700 Fenwick Lane, Suite 500, Larkmere Park, NY 10999</p>
      <div class="band"></div>
    </div>
  </section>

  <section class="sheet letterhead" style="left:297px">
    <div class="brand"><span class="brand-dot"></span><span class="brand-name">Velmoran Group</span></div>
    <div class="decor" role="img" aria-label="Soft white emblem shape as watermark"></div>
    <div class="sheet-footer">
      <div class="band"></div>
      <span class="band-dot"></span>
    </div>
  </section>

  <section class="sheet fax-sheet" style="left:552px">
    <div class="brand"><span class="brand-dot"></span><span class="brand-name">Velmoran Group</span></div>
    <h2 class="fax-title">FAX</h2>
    <div class="fax-fields">
      <span>To:</span><span>From:</span>
      <span>Fax:</span><span>Pages:</span>
      <span>Phone:</span><span>Date:</span>
      <span>Re:</span><span>CC:</span>
    </div>
    <div class="fax-checks">
      <span><i></i>Urgent</span><span><i></i>For Review</span><span><i></i>Please Comment</span><span><i></i>Please Reply</span>
    </div>
    <div class="fax-rule"></div>
    <div class="sheet-footer"><div class="band"></div></div>
  </section>

  <div class="envelope envelope-back">
    <svg class="flap" viewBox="0 0 346 78" preserveAspectRatio="none">
      <defs><linearGradient id="flapGrad" x1="0" x2="1"><stop offset="0" stop-color="#0d2a5c"/><stop offset=".6" stop-color="#1d5fae"/><stop offset="1" stop-color="#0d2a5c"/></linearGradient></defs>
      <polygon points="0,0 346,0 346,10 173,70 0,10" fill="url(#flapGrad)"/>
      <circle cx="173" cy="40" r="9" fill="#6fa6dd"/>
    </svg>
  </div>

  <div class="envelope envelope-front">
    <div class="brand"><span class="brand-dot"></span><span class="brand-name">Velmoran Group</span></div>
    <div class="decor" role="img" aria-label="Soft white emblem shape as watermark"></div>
    <div class="band"></div>
  </div>

  <div class="cards">
    <div class="card card-light">
      <div class="brand"><span class="brand-dot"></span><span class="brand-name">Velmoran Group</span></div>
      <div class="card-contact"><strong>Peter L. Dunmore</strong><br>Founder<br>pete@velmoran-example.com</div>
      <div class="band"></div>
    </div>
    <div class="card card-light">
      <div class="brand"><span class="brand-dot"></span><span class="brand-name">Velmoran Group</span></div>
      <div class="card-contact"><strong>Peter L. Dunmore</strong><br>2700 Fenwick Lane, Suite 500<br>www.velmoran-example.com</div>
      <div class="band"></div>
    </div>
    <div class="card card-light">
      <div class="brand"><span class="brand-dot"></span><span class="brand-name">Velmoran Group</span></div>
      <div class="card-contact"><strong>Peter L. Dunmore</strong><br>Larkmere Park, NY 10999<br>pete@velmoran-example.com</div>
      <div class="band"></div>
    </div>
    <div class="card card-dark">
      <div class="brand"><span class="brand-dot"></span><span class="brand-name">Velmoran Group</span></div>
    </div>
    <div class="card card-light">
      <div class="brand"><span class="brand-dot"></span><span class="brand-name">Velmoran Group</span></div>
      <div class="card-contact"><strong>Peter L. Dunmore</strong><br>Founder<br>www.velmoran-example.com</div>
      <div class="band"></div>
    </div>
    <div class="card card-dark">
      <div class="brand"><span class="brand-dot"></span><span class="brand-name">Velmoran Group</span></div>
      <div class="card-contact"><strong>Peter L. Dunmore</strong><br>Founder</div>
    </div>
  </div>

</div>
</body>
</html>
```